New telco company needs a product page

We need to design two pages - one index and one inner.

We are a new telco company and we have developed our own phone. We will be selling our services and the phone on this site.

The design should be easy to understand and use, following the latest trends in Web design, be clean. It should communicate professionalism and integrity.

The name of our company is VORO which stands for Values Open Routes Onward. The design should follow this principle.

Our company logo is attached. I can send it in other colors/sizes - let me know.

Target Market(s)

Aging population (70+), middle-aged with parents and grandparents.

Industry/Entity Type

It Company

Requirements
Must have
• index page, inner page, flat, clean, Panelo 7 style / ZEB style (zebtrov.com), easy navigation, fluid layout, CSS, tableless
Should not have
• should not use old fonts, should not use old-style design, should not have animation, should not look like QRT or Gubble (too busy)

```html
<!DOCTYPE html>
<html lang="en">
<head>
<meta charset="utf-8">
<title>VORO Halden X2</title>
<link rel="stylesheet" href="https://fonts.googleapis.com/css2?family=Ubuntu:wght@300;400;500;700&display=swap">
<style>
:root{
  --nav-bg:#050607;
  --white:#ffffff;
  --ink:#111111;
  --muted:#b9b9b9;
  --footer-ink:#555555;
  --rule:#e2e2e2;
  --accent:#2f80c1;
  --sky:#b9c2c0;
  --haze:#c9bf9d;
  --hill:#7d7150;
  --ground:#5f5639;
  --device:#1b1c1e;
  --spec-bg:rgba(62,56,40,.55);
}
*{margin:0;padding:0;box-sizing:border-box}
html,body{width:1200px;height:805px;overflow:hidden;background:var(--white);font-family:"Ubuntu",Arial,sans-serif}
.page{position:relative;width:1200px;height:805px}

.site-nav{position:absolute;left:0;top:0;width:1200px;height:78px;background:var(--nav-bg)}
.brand{position:absolute;left:197px;top:16px;display:flex;align-items:center;gap:8px;color:var(--white);font-weight:300;font-size:38px;letter-spacing:-1px}
.brand-mark{width:22px;height:22px;border:2px solid var(--white)}
.menu{position:absolute;top:33px;left:0;list-style:none}
.menu li{position:absolute;white-space:nowrap;color:var(--white);font-size:12px;font-weight:700}
.menu .caret{display:inline-block;margin-left:4px;vertical-align:1px}
.lang{position:absolute;left:877px;top:34px;color:#d8d8d8;font-size:11px;display:flex;align-items:center;gap:7px}
.flag{width:12px;height:8px;background:#c53a3a;border-top:3px solid #3a4f9a}
.search{position:absolute;left:983px;top:33px}

.hero{position:absolute;left:0;top:78px;width:1200px;height:552px;
  background:linear-gradient(180deg,var(--sky) 0%,#cfcab0 30%,var(--haze) 48%,var(--hill) 70%,var(--ground) 100%)}
.hero-device{position:absolute;left:198px;top:188px;width:248px;height:352px;border-radius:26px;
  background:linear-gradient(160deg,#3a3b3e 0%,var(--device) 60%,#0c0c0d 100%)}
.hero-copy{position:absolute;left:523px;top:190px;color:var(--ink)}
.hero-model{font-size:30px;font-weight:400;line-height:40px}
.hero-model b{font-weight:700}
.hero-title{font-size:46px;font-weight:700;line-height:49px;letter-spacing:0;margin-top:6px}
.specs{position:absolute;left:524px;top:372px;width:331px;height:81px;background:var(--spec-bg);list-style:none;
  display:grid;grid-template-columns:129px 160px;grid-auto-rows:17px;align-content:start;row-gap:9px;padding:18px 0 0 24px;color:var(--white);font-size:14px;line-height:17px}
.cta-row{position:absolute;left:523px;top:475px;display:flex;align-items:center}
.cta{display:flex;align-items:center;gap:14px;height:41px;width:193px;padding-left:14px;background:var(--accent);color:var(--white);font-size:16px;text-decoration:none}
.or{margin-left:15px;color:var(--white);font-size:12px}
.video-link{margin-left:16px;color:var(--white);font-size:12px;font-weight:500;text-decoration:none}

.product-tabs{position:absolute;left:0;top:630px;width:1200px;height:77px}
.tab{position:absolute;top:0;height:76px;padding-top:26px;font-size:20px;color:var(--muted);white-space:nowrap}
.tab b{font-weight:700}
.tab.active{color:var(--ink);background:var(--white);box-shadow:8px 0 10px -6px rgba(0,0,0,.15)}
.tabs-rule{position:absolute;left:198px;top:706px;width:804px;height:1px;background:var(--rule)}

.site-footer{position:absolute;left:0;top:732px;width:1200px;color:var(--footer-ink);font-size:11px}
.footer-title{color:var(--ink);font-size:12px;font-weight:500;margin-bottom:5px}
.join{position:absolute;left:199px;top:0}
.socials{position:absolute;left:389px;top:14px;display:flex;gap:12px}
.socials span{width:13px;height:13px;border-radius:50%;background:#8a8a8a}
.support{position:absolute;left:523px;top:0}
.support .phones span{margin-right:14px}
.copyright{position:absolute;left:778px;top:21px;font-size:9.6px;white-space:nowrap}
</style>
</head>
<body>
<div class="page">
  <header class="site-nav">
    <div class="brand"><span>voro</span><span class="brand-mark"></span></div>
    <ul class="menu">
      <li style="left:358px">PRODUCTS<svg class="caret" width="10" height="6" viewBox="0 0 10 6"><path d="M1 1l4 4 4-4" stroke="#2f80c1" stroke-width="2" fill="none"/></svg></li>
      <li style="left:484px">WHY VORO</li>
      <li style="left:598px">COMMUNITY</li>
      <li style="left:714px">SUPPORT</li>
    </ul>
    <div class="lang">Language <span class="flag"></span></div>
    <svg class="search" width="14" height="14" viewBox="0 0 14 14"><circle cx="5.5" cy="5.5" r="4.2" stroke="#fff" stroke-width="2" fill="none"/><path d="M8.6 8.6l4 4" stroke="#fff" stroke-width="2.4" stroke-linecap="round"/></svg>
  </header>

  <section class="hero" role="img" aria-label="Misty rolling hills landscape at sunrise"></section>
  <div class="hero-device" role="img" aria-label="Two black VORO Halden X2 smartphones, front view"></div>
  <div class="hero-copy">
    <p class="hero-model"><b>VORO</b> Halden X2</p>
    <h1 class="hero-title">POWERFULL WITH<br>QUAD CHIP</h1>
  </div>
  <ul class="specs">
    <li>4.3" Home Screen</li><li>Compact One-Hand Use</li>
    <li>Quad Core Chip</li><li>Dual Frontal Speakers</li>
  </ul>
  <div class="cta-row">
    <a class="cta" href="#">Meet The Halden X2 <svg width="7" height="11" viewBox="0 0 7 11"><path d="M1 1l4.5 4.5L1 10" stroke="#fff" stroke-width="2" fill="none"/></svg></a>
    <span class="or">Or</span>
    <a class="video-link" href="#">Watch this video</a>
  </div>

  <nav class="product-tabs">
    <div class="tab active" style="left:180px;padding-left:19px;width:186px"><b>VORO</b> Halden X2</div>
    <div class="tab" style="left:390px"><b>VORO</b> Halden Mini</div>
    <div class="tab" style="left:593px"><b>VORO</b> Halden Music S</div>
    <div class="tab" style="left:829px"><b>VORO</b> Halden X3</div>
  </nav>
  <div class="tabs-rule"></div>

  <footer class="site-footer">
    <div class="join"><p class="footer-title">Join VORO online</p><p>You can find out the latest news</p></div>
    <div class="socials"><span></span><span></span><span></span></div>
    <div class="support"><p class="footer-title">Customer Support</p><p class="phones"><span>+010 5550 1234</span><span>+010 5550 4321</span></p></div>
    <p class="copyright">Copyright © 2013 StudioHarbor. All right reserved.</p>
  </footer>
</div>
</body>
</html>
```